Venbrook Finishes website

Epoxy Resin Flooring for home renovations and commercial property.
3 page website homepage, contact us and gallery with a link to Photofeed.
Looking for someone to create a visually pleasing website for home transformation and design. I have attached some designs of completed work however I can send you many more. Use colour and don’t inspiration from the logo. If happy with stage one we will add a commercial page as a new project.

Target Market(s)

Homeowners that want to improve their home or rental property

Industry/Entity Type

Home improvements

Coding

Coded - Design and coding required

Number of Pages Required

3 page

Requirements
Must have
• Home Page, Contact Us page and showcase / gallery page
Nice to have
• I would like the colour theme to be taken from the logo, a clean finish with artistic usuals to get homeowners excited about their project

```html
<!DOCTYPE html>
<html lang="en">
<head>
<meta charset="utf-8">
<title>Venbrook Finishes – Epoxy Resin Flooring</title>
<link href="https://fonts.googleapis.com/css2?family=Montserrat:wght@300;400;500;600;700;800&display=swap" rel="stylesheet">
<style>
:root{
  --red:#e8141b;
  --red-dark:#c3161c;
  --ink:#111111;
  --text:#2a2a2a;
  --muted:#555;
  --light:#eeeeee;
  --white:#ffffff;
  --black:#0b0b0b;
}
*{box-sizing:border-box;margin:0;padding:0}
html,body{width:1200px;height:3128px;overflow:hidden}
body{position:relative;font-family:'Montserrat',sans-serif;color:var(--text);background:var(--white)}
.abs{position:absolute}

/* header */
.site-header{position:absolute;left:0;top:0;width:1200px;height:86px;background:var(--white);border-bottom:1px solid #e4e4e4;z-index:5}
.brand{position:absolute;display:flex;align-items:center;gap:12px}
.brand-mark{width:61px;height:65px;background:var(--red)}
.brand-name{font-weight:800;font-size:22px;line-height:1;color:var(--ink);text-transform:uppercase;letter-spacing:.5px}
.brand-phone{font-size:15px;font-weight:500;letter-spacing:1.5px;color:var(--ink);margin-top:6px}
.main-nav a{position:absolute;top:35px;font-size:14px;font-weight:600;color:var(--ink);text-decoration:none;transform:translateX(-50%);white-space:nowrap}
.main-nav a.active{color:var(--red)}
.main-nav a.active::after{content:"";position:absolute;left:0;right:0;bottom:-9px;height:2px;background:var(--red)}
.nav-sep{position:absolute;top:36px;width:1px;height:14px;background:#bbb}
.social-dot{position:absolute;left:908px;top:32px;width:22px;height:22px;border:2px solid var(--ink);border-radius:50%}
.call-box{position:absolute;left:968px;top:0;width:232px;height:86px;background:var(--red);clip-path:polygon(20px 0,100% 0,100% 100%,0 100%)}
.call-slash{position:absolute;left:966px;top:12px;width:3px;height:76px;background:var(--ink);transform:skewX(-15deg)}
.call-icon{position:absolute;left:1000px;top:26px;width:34px;height:34px;border-radius:50%;background:var(--white)}
.call-label{position:absolute;left:1042px;top:23px;color:var(--white);font-size:13px;font-weight:400}
.call-num{position:absolute;left:1042px;top:41px;color:var(--white);font-size:17px;font-weight:700}

/* hero */
.hero{position:absolute;left:0;top:86px;width:1200px;height:654px;background:linear-gradient(180deg,#6d7178 0%,#4e5866 40%,#2f4468 70%,#243a63 100%)}
.hero-eyebrow{position:absolute;left:0;width:1200px;top:245px;text-align:center;color:var(--white);font-size:17px;letter-spacing:2px;font-weight:400}
.eyebrow-line{display:inline-block;width:46px;height:2px;background:var(--red);vertical-align:middle;margin:0 8px}
.hero-title{position:absolute;left:0;width:1200px;top:278px;text-align:center;color:var(--white);line-height:44px}
.hero-title .thin{display:block;font-weight:300;font-size:42px;letter-spacing:.5px}
.hero-title .bold{display:block;font-weight:800;font-size:42px}
.pill{position:absolute;height:50px;border-radius:25px;background:var(--red);color:var(--white);font-weight:700;font-size:15px;letter-spacing:.5px;display:flex;align-items:center;justify-content:center;padding-right:30px;overflow:hidden}
.pill::after{content:"";position:absolute;right:14px;top:14px;width:14px;height:14px;border-radius:50%;background:rgba(255,255,255,.35);box-shadow:10px 10px 0 -2px rgba(255,255,255,.25)}
.divider-red{position:absolute;left:600px;top:698px;width:2px;height:67px;background:var(--red)}

/* about */
.about-photo{position:absolute;left:115px;top:778px;width:400px;height:506px;border-radius:24px;background:linear-gradient(180deg,#dfe2e6 0%,#8d929a 45%,#454a53 85%,#5d7040 100%)}
.eyebrow{font-size:17px;letter-spacing:2px;color:var(--ink);font-weight:400}
.section-title{font-size:34px;font-weight:700;color:var(--ink);text-transform:uppercase}
.section-title .accent{color:var(--red)}
.about-sub{position:absolute;left:598px;top:952px;width:480px;font-size:21px;font-weight:600;color:var(--ink);line-height:29px}
.about-copy{position:absolute;left:598px;width:530px;font-size:19px;line-height:27px;color:var(--muted)}

/* gallery */
.gallery-bg{position:absolute;left:0;top:1369px;width:1200px;height:775px;background:linear-gradient(160deg,#f3f3f3,#e6e6e6 50%,#f1f1f1)}
.chevron{position:absolute;top:1728px;width:24px;height:52px}

/* contact */
.contact-band{position:absolute;left:0;top:2144px;width:1200px;height:666px;background:linear-gradient(115deg,#b3181e 0%,#d52027 45%,#e83a3c 100%)}
.contact-intro{position:absolute;left:128px;top:2360px;width:440px;color:var(--white);font-size:19px;line-height:27px;font-weight:400}
.contact-item{position:absolute;left:128px;display:flex;align-items:center;gap:18px;color:var(--white)}
.contact-item .ico{width:46px;height:46px;border-radius:50%;background:var(--white);flex:none}
.contact-item small{display:block;font-size:15px;font-weight:400}
.contact-item strong{display:block;font-size:19px;font-weight:600}
.form-card{position:absolute;left:607px;top:2286px;width:497px;height:389px;background:var(--black);border-radius:8px}
.form-title{position:absolute;left:49px;top:38px;color:var(--white);font-size:20px;font-weight:700}
.field{position:absolute;background:var(--white);font-size:13px;color:#444;padding:12px 16px;font-weight:400}

/* footer */
.foot-rule{position:absolute;height:1px;background:#bdbdbd}
.foot-nav{position:absolute;top:2868px;font-size:16px;font-weight:700;color:var(--ink);transform:translateX(-50%)}
.foot-dot{position:absolute;top:2873px;width:6px;height:6px;border-radius:50%;background:var(--red)}
.foot-item{position:absolute;top:2958px;display:flex;align-items:center;gap:10px}
.foot-item .ico{width:32px;height:32px;border-radius:50%;background:var(--red);flex:none}
.foot-item small{display:block;font-size:11px;font-weight:700;color:var(--ink)}
.foot-item span{display:block;font-size:15px;color:var(--text)}
.copyright{position:absolute;left:0;width:1200px;top:3054px;text-align:center;font-size:12px;color:var(--ink)}
.copyright u{text-underline-offset:2px}
.to-top{position:absolute;left:1018px;top:3049px;width:36px;height:36px;border-radius:50%;background:#eee;border:1px solid #ddd}
</style>
</head>
<body>

<header class="site-header">
  <div class="brand" style="left:120px;top:10px">
    <div class="brand-mark"></div>
    <div>
      <div class="brand-name">Venbrook Finishes</div>
      <div class="brand-phone">0455 218 906</div>
    </div>
  </div>
  <nav class="main-nav">
    <a href="#" class="active" style="left:502px">HOME</a>
    <span class="nav-sep" style="left:561px"></span>
    <a href="#" style="left:632px">GALLERY</a>
    <span class="nav-sep" style="left:700px"></span>
    <a href="#" style="left:787px">CONTACT US</a>
    <span class="nav-sep" style="left:861px"></span>
  </nav>
  <span class="social-dot" aria-label="Photofeed"></span>
  <div class="call-box"></div>
  <div class="call-slash"></div>
  <div class="call-icon">
    <svg viewBox="0 0 24 24" width="34" height="34"><path d="M8 6.5c.6-.6 1.4-.5 1.8.2l1.1 1.9c.3.6.2 1.2-.3 1.6l-.8.7c.6 1.4 1.8 2.6 3.2 3.3l.7-.8c.4-.5 1.1-.6 1.6-.3l1.9 1.1c.7.4.8 1.3.2 1.8l-1 1c-1 1-4 .4-6.6-2.2S6 8.5 7 7.5z" fill="#e8141b"/></svg>
  </div>
  <div class="call-label">CALL US NOW</div>
  <div class="call-num">0455 218 906</div>
</header>

<section class="hero" role="img" aria-label="Finished dark blue epoxy tile-effect patio beside a house"></section>
<svg class="abs" style="left:0;top:650px" width="1200" height="92" viewBox="0 650 1200 92"><path d="M0 678 C300 660 450 735 600 735 C750 735 900 660 1200 678 L1200 742 L0 742Z" fill="#fff"/></svg>
<div class="hero-eyebrow"><span class="eyebrow-line"></span>WELCOME TO VENBROOK FINISHES<span class="eyebrow-line"></span></div>
<h1 class="hero-title"><span class="thin">EPOXY RESIN FLOORING FOR</span><span class="bold">HOME RENOVATIONS AND</span><span class="bold">COMMERCIAL PROPERTY</span></h1>
<a class="pill" style="left:505px;top:431px;width:190px">CONTACT US</a>
<div class="divider-red"></div>

<!-- about -->
<div class="about-photo" role="img" aria-label="Photo of a finished grey epoxy floor in a hallway and entry"></div>

<div class="abs eyebrow" style="left:594px;top:861px">WHO WE ARE <span style="display:inline-block;width:46px;height:2px;background:var(--red);vertical-align:middle;margin-left:10px"></span></div>
<h2 class="abs section-title" style="left:594px;top:887px"><span class="accent">About</span> Venbrook Finishes</h2>
<p class="about-sub">Epoxy Resin Flooring for home renovations and commercial property</p>
<p class="about-copy" style="top:1021px">Lorem ipsum dolor sit amet, consectetur adipiscing elit, sed do eiusmod tempor incididunt ut labore et dolore magna aliqua. Quis ipsum suspendisse ultrices</p>
<p class="about-copy" style="top:1132px">Lorem ipsum dolor sit amet, consectetur adipiscing elit, sed do eiusmod tempor incididunt ut labore et dolore magna aliqua. Quis ipsum suspendisse ultrices gravida.</p>

<!-- gallery -->
<div class="gallery-bg"></div>
<svg class="abs" style="left:0;top:1320px" width="1200" height="52" viewBox="0 1320 1200 52"><path d="M0 1370 C300 1370 450 1326 600 1326 C750 1326 900 1370 1200 1370Z" fill="#f1f1f1"/></svg>
<div class="abs eyebrow" style="left:0;width:1200px;top:1402px;text-align:center"><span class="eyebrow-line"></span>OUR WORK<span class="eyebrow-line"></span></div>
<h2 class="abs section-title" style="left:0;width:1208px;top:1428px;text-align:center"><span class="accent">Project</span> Gallery</h2>

<svg class="abs" style="left:100px;top:1510px" width="1010" height="500" viewBox="100 1510 1010 500" role="img" aria-label="Gallery of completed epoxy floors: patios, porches and a café floor">
  <defs>
    <linearGradient id="g1" x1="0" y1="0" x2="0" y2="1"><stop offset="0" stop-color="#dfe2e5"/><stop offset=".5" stop-color="#4a4d55"/><stop offset="1" stop-color="#6f8a3a"/></linearGradient>
    <linearGradient id="g2" x1="0" y1="0" x2="0" y2="1"><stop offset="0" stop-color="#5b5e64"/><stop offset="1" stop-color="#8e8f92"/></linearGradient>
    <linearGradient id="g3" x1="0" y1="0" x2="0" y2="1"><stop offset="0" stop-color="#d6dadd"/><stop offset=".45" stop-color="#8a5b4a"/><stop offset="1" stop-color="#3d4048"/></linearGradient>
    <linearGradient id="g4" x1="0" y1="0" x2="0" y2="1"><stop offset="0" stop-color="#7d6a60"/><stop offset=".5" stop-color="#c7c0b5"/><stop offset="1" stop-color="#d1cbc2"/></linearGradient>
    <linearGradient id="g5" x1="0" y1="0" x2="0" y2="1"><stop offset="0" stop-color="#b9bec5"/><stop offset=".5" stop-color="#33466a"/><stop offset="1" stop-color="#263a60"/></linearGradient>
  </defs>
  <polygon points="270,1515 429,1674 270,1833 111,1674" fill="url(#g1)"/>
  <polygon points="604,1515 763,1674 604,1833 445,1674" fill="url(#g2)"/>
  <polygon points="945,1515 1104,1674 945,1833 786,1674" fill="url(#g3)"/>
  <polygon points="438,1690 597,1849 438,2008 279,1849" fill="url(#g4)"/>
  <polygon points="773,1690 932,1849 773,2008 614,1849" fill="url(#g5)"/>
</svg>
<svg class="chevron" style="left:96px" viewBox="0 0 24 52"><path d="M22 2 L2 26 L22 50" fill="none" stroke="#222" stroke-width="2"/></svg>
<svg class="chevron" style="left:1080px" viewBox="0 0 24 52"><path d="M2 2 L22 26 L2 50" fill="none" stroke="#222" stroke-width="2"/></svg>
<a class="pill" style="left:510px;top:2038px;width:190px">VIEW MORE</a>

<!-- contact -->
<section class="contact-band" role="img" aria-label="Red-tinted interior with a freshly coated epoxy floor"></section>
<svg class="abs" style="left:0;top:2760px" width="1200" height="52" viewBox="0 2760 1200 52"><path d="M0 2807 C300 2807 450 2764 600 2764 C750 2764 900 2807 1200 2807 L1200 2812 L0 2812Z" fill="#fff"/></svg>
<div class="abs eyebrow" style="left:128px;top:2275px;color:#fff">GET IN TOUCH <span style="display:inline-block;width:46px;height:2px;background:#fff;vertical-align:middle;margin-left:6px"></span></div>
<h2 class="abs section-title" style="left:128px;top:2303px;color:#fff">Contact Venbrook</h2>
<p class="contact-intro">Lorem ipsum dolor sit amet, consectetur adip-iscing elit sed do eiusmod temp</p>
<div class="contact-item" style="top:2451px">
  <svg class="ico" viewBox="0 0 24 24"><path d="M8 6.5c.6-.6 1.4-.5 1.8.2l1.1 1.9c.3.6.2 1.2-.3 1.6l-.8.7c.6 1.4 1.8 2.6 3.2 3.3l.7-.8c.4-.5 1.1-.6 1.6-.3l1.9 1.1c.7.4.8 1.3.2 1.8l-1 1c-1 1-4 .4-6.6-2.2S6 8.5 7 7.5z" fill="#d52027"/></svg>
  <div><small>Phone Number</small><strong style="font-weight:700">0455 218 906</strong></div>
</div>
<div class="contact-item" style="top:2524px">
  <svg class="ico" viewBox="0 0 24 24"><rect x="6" y="8" width="12" height="8" rx="1" fill="none" stroke="#d52027" stroke-width="1.4"/><path d="M6 8.5l6 4.5 6-4.5" fill="none" stroke="#d52027" stroke-width="1.4"/></svg>
  <div><small>Email address</small><strong>info@venbrookfinishes.com</strong></div>
</div>
<div class="contact-item" style="top:2596px">
  <svg class="ico" viewBox="0 0 24 24"><path d="M12 5.5a4.5 4.5 0 0 1 4.5 4.5c0 3.2-4.5 8-4.5 8s-4.5-4.8-4.5-8A4.5 4.5 0 0 1 12 5.5z" fill="#d52027"/><circle cx="12" cy="10" r="1.7" fill="#fff"/></svg>
  <div><small>Location</small><strong>123 Street Avenue address line</strong></div>
</div>

<div class="form-card">
  <div class="form-title">LEAVE US A MESSAGE</div>
  <div class="field" style="left:46px;top:89px;width:200px;height:40px">First Name</div>
  <div class="field" style="left:254px;top:89px;width:199px;height:40px">Last Name</div>
  <div class="field" style="left:46px;top:141px;width:200px;height:39px">Email address</div>
  <div class="field" style="left:254px;top:141px;width:199px;height:39px">Phone</div>
  <div class="field" style="left:46px;top:189px;width:407px;height:86px">Message</div>
  <a class="pill" style="left:46px;top:295px;width:191px;height:44px;font-size:14px">SEND MESSAGE</a>
</div>

<!-- footer -->
<footer>
  <div class="foot-rule" style="left:109px;top:2845px;width:368px"></div>
  <div class="foot-rule" style="left:109px;top:2905px;width:368px"></div>
  <div class="foot-rule" style="left:718px;top:2845px;width:369px"></div>
  <div class="foot-rule" style="left:718px;top:2905px;width:369px"></div>
  <a class="foot-nav" style="left:197px">HOME</a>
  <span class="foot-dot" style="left:263px"></span>
  <a class="foot-nav" style="left:344px">ABOUT US</a>
  <a class="foot-nav" style="left:805px">GALLERY</a>
  <span class="foot-dot" style="left:879px"></span>
  <a class="foot-nav" style="left:969px">CONTACT US</a>
  <div class="brand" style="left:505px;top:2843px;gap:10px">
    <div class="brand-mark" style="width:60px;height:65px"></div>
    <div>
      <div class="brand-name" style="font-size:16px">Venbrook<br>Finishes</div>
      <div class="brand-phone" style="font-size:13px;margin-top:4px">0455 218 906</div>
    </div>
  </div>

  <div class="foot-item" style="left:143px"><svg class="ico" viewBox="0 0 24 24"><path d="M8 6.5c.6-.6 1.4-.5 1.8.2l1.1 1.9c.3.6.2 1.2-.3 1.6l-.8.7c.6 1.4 1.8 2.6 3.2 3.3l.7-.8c.4-.5 1.1-.6 1.6-.3l1.9 1.1c.7.4.8 1.3.2 1.8l-1 1c-1 1-4 .4-6.6-2.2S6 8.5 7 7.5z" fill="#fff"/></svg><div><small>PHONE</small><span>0455 218 906</span></div></div>
  <div class="foot-item" style="left:352px"><svg class="ico" viewBox="0 0 24 24"><rect x="6" y="8" width="12" height="8" rx="1" fill="none" stroke="#fff" stroke-width="1.4"/><path d="M6 8.5l6 4.5 6-4.5" fill="none" stroke="#fff" stroke-width="1.4"/></svg><div><small>EMAIL ADDRESS</small><span>info@venbrookfinishes.com</span></div></div>
  <div class="foot-item" style="left:624px"><svg class="ico" viewBox="0 0 24 24"><path d="M12 5.5a4.5 4.5 0 0 1 4.5 4.5c0 3.2-4.5 8-4.5 8s-4.5-4.8-4.5-8A4.5 4.5 0 0 1 12 5.5z" fill="#fff"/><circle cx="12" cy="10" r="1.7" fill="#e8141b"/></svg><div><small>LOCATION</small><span>123 Street Avenue address</span></div></div>
  <div class="foot-item" style="left:911px"><span class="ico"></span><div><small>PHOTOFEED</small><span>@venbrookfinishes</span></div></div>

  <div class="foot-rule" style="left:126px;top:3030px;width:959px"></div>
  <p class="copyright">Copyright © 2024 <u>Venbrook Finishes</u>. All Right Reserved</p>
  <div class="to-top"><svg viewBox="0 0 36 36" width="34" height="34"><path d="M13 20l5-5 5 5" fill="none" stroke="#555" stroke-width="1.6"/></svg></div>
</footer>

</body>
</html>
```